Palvette International needs a book cover

I am self publishing a book titles entitled, Quiet Threads Through Carrying and Raising. Pressline Yard is ready to do the print, but I did not like their design. I am attaching the picture I want on the front.

Hello all - Thank you all for your beautiful designs.  I am closing this project in 24 hours. I will be making my final selection then.  I apologize for closing earlier than my deadline.  This is my first project and I have learned a lot:)  I will be back with more projects!

```html
<!DOCTYPE html>
<html lang="en">
<head>
<meta charset="utf-8">
<title>Quiet Threads – Back Cover</title>
<link href="https://fonts.googleapis.com/css2?family=Cormorant+Garamond:ital,wght@1,500;1,600&family=EB+Garamond:wght@400&display=swap" rel="stylesheet">
<style>
  :root {
    --purple-light: #8a3a9e;
    --purple-mid: #6c1a7e;
    --purple-deep: #4e0a5e;
    --spine-deep: #46085a;
    --cream: #f4e7ad;
    --white: #ffffff;
    --photo-light: #e8e4ea;
    --photo-dark: #2a2430;
  }
  html, body {
    margin: 0;
    padding: 0;
    width: 900px;
    height: 1200px;
    overflow: hidden;
    background: #ffffff;
  }
  .cover {
    position: relative;
    width: 900px;
    height: 1200px;
    display: flex;
    background: radial-gradient(ellipse 70% 60% at 58% 48%, var(--purple-light) 0%, var(--purple-mid) 45%, var(--purple-deep) 100%);
    color: var(--white);
    overflow: hidden;
  }
  .spine {
    width: 78px;
    flex: none;
    background: linear-gradient(90deg, var(--spine-deep), var(--purple-mid) 70%, var(--purple-deep));
    border-right: 1px solid rgba(255,255,255,0.12);
    display: flex;
    align-items: center;
    justify-content: space-between;
    writing-mode: vertical-rl;
    padding: 60px 0 60px;
    box-sizing: border-box;
  }
  .spine-title {
    font-family: "Cormorant Garamond", serif;
    font-style: italic;
    font-weight: 600;
    font-size: 44px;
    letter-spacing: 1px;
  }
  .spine-author {
    font-family: "Cormorant Garamond", serif;
    font-style: italic;
    font-weight: 500;
    font-size: 28px;
  }
  .back {
    flex: 1;
    display: flex;
    flex-direction: column;
    align-items: center;
    text-align: center;
    padding: 120px 70px 0;
    box-sizing: border-box;
  }
  .book-title {
    margin: 0;
    font-family: "Cormorant Garamond", serif;
    font-style: italic;
    font-weight: 600;
    font-size: 112px;
    line-height: 0.95;
  }
  .book-title span { display: block; }
  .book-title .line-two { padding-left: 40px; }
  .tagline {
    margin: 56px 0 0;
    font-family: "Cormorant Garamond", serif;
    font-style: italic;
    font-weight: 500;
    font-size: 40px;
    line-height: 1.15;
    color: var(--cream);
  }
  .blurb {
    margin: 38px 0 0;
    font-family: "EB Garamond", serif;
    font-size: 23px;
    line-height: 1.3;
    max-width: 680px;
  }
  .blurb + .blurb { margin-top: 26px; }
  .author-photo {
    margin-top: 56px;
    width: 122px;
    height: 142px;
    background: linear-gradient(160deg, var(--photo-light) 0%, #b9b3be 55%, var(--photo-dark) 100%);
    box-shadow: 0 2px 6px rgba(0,0,0,0.3);
  }
  .author-bio {
    margin: 44px 0 0;
    font-family: "EB Garamond", serif;
    font-size: 21px;
    line-height: 1.3;
    max-width: 640px;
  }
</style>
</head>
<body>
  <div class="cover">
    <div class="spine">
      <span class="spine-title">Quiet Threads</span>
      <span class="spine-author">Dana Lee Marlowe</span>
    </div>
    <main class="back">
      <h1 class="book-title"><span>Quiet</span><span class="line-two">Threads</span></h1>
      <p class="tagline">“Mothers are the spiritual glue<br>that holds a family together.”</p>
      <p class="blurb">When we grow older and learn more about science and the things we can easily understand and touch, we stray from a spiritual connection. This book is about the journey back in an intentional and purposeful way using pregnancy and motherhood as a vehicle to get us there.</p>
      <p class="blurb">Quiet Threads Through Carrying and Raising enhance a women’s journey as we go deeper into our soul to love ourselves unconditionally each moment. Only then can we begin to love our child and others with the same unconditional love.</p>
      <div class="author-photo" role="img" aria-label="Author portrait photograph"></div>
      <p class="author-bio">Dana Lee Marlowe is the proud mother of three amazing and beautiful children, Tessa, Owen and Clara. Born and raised in Alder Falls, Maine, Dana Lee now resides in Kestrel Ridge, Virginia with her fiancé, Reed and youngest daughter, Clara. She lives life fully as a passionate educator, engineer and writer.</p>
    </main>
  </div>
</body>
</html>
```